Lumo4Kart - a fintech company - business card

We need a business card design for our Payments Technology company in Sydney, Australia. We provide business with payment solutions expanding across EFTPOS machines, online payment gateways and mobile payment solutions. We would like to see designs that are clean, classy and professional.
Target Market(s)
Business professionals, executives, c-suite
Industry/Entity Type
Fintech
Contact Information for Business Card
Will be on 400gsm. Logo will most likely be spot gloss unless designer recommends otherwise.
Font styles to use
Sans Serif
Requirements
Must have
- We need our website (lumo4kart.com.au), email (contact@lumo4kart.com.au), mobile (0432 587 904) and direct phone number (02 6815 3927) to feature on the card along with our logo (attached) and the words "EFTPOS | ONLINE | MOBILE"
- Font = Roboto

```html
<!DOCTYPE html>
<html lang="en">
<head>
<meta charset="utf-8">
<title>Lumo4Kart business card</title>
<link href="https://fonts.googleapis.com/css2?family=Roboto:wght@400;500;700;900&display=swap" rel="stylesheet">
<style>
  :root {
    --ink: #2b2a28;
    --gold: #d8b56f;
    --paper: #ffffff;
  }
  * { margin: 0; padding: 0; box-sizing: border-box; }
  html, body { width: 1200px; height: 1026px; overflow: hidden; background: var(--ink); }
  body { position: relative; font-family: "Roboto", sans-serif; }

  .card { position: absolute; top: 206px; width: 381px; height: 588px; overflow: hidden; background: var(--ink); }
  .card--front { left: 200px; }
  .card--back { left: 651px; }

  /* Front */
  .front__paper { position: absolute; left: 0; top: 0; width: 100%; height: 227px; background: var(--paper); }
  .front__tab {
    position: absolute; left: 228px; top: 145px; width: 153px; height: 208px;
    background: var(--gold); border-radius: 46px 0 0 46px;
    display: flex; align-items: center; justify-content: center;
  }
  .front__tab-name { color: var(--ink); font-weight: 700; font-size: 14px; letter-spacing: 2px; }

  .vertical {
    position: absolute; white-space: nowrap;
    writing-mode: vertical-rl; transform: rotate(180deg);
  }
  .front__name {
    left: 44px; bottom: 294px; line-height: 30px;
    color: var(--gold); font-weight: 900; font-size: 26px; letter-spacing: 9px;
  }
  .front__dot {
    display: inline-block; width: 8px; height: 8px; border-radius: 50%;
    background: var(--gold); margin-bottom: 10px; vertical-align: middle;
  }
  .front__tagline {
    left: 80px; bottom: 319px; line-height: 10px;
    color: var(--gold); font-weight: 500; font-size: 7px; letter-spacing: 1.6px;
  }

  .contact { position: absolute; left: 42px; top: 425px; list-style: none; }
  .contact__item {
    position: relative; padding-left: 14px; height: 39px;
    color: var(--gold); font-size: 14px; letter-spacing: 2px; line-height: 16px;
  }
  .contact__item::before {
    content: ""; position: absolute; left: 0; top: 7px; width: 3px; height: 3px;
    border-radius: 50%; background: var(--gold);
  }

  /* Back */
  .back__paper { position: absolute; left: 0; top: 360px; width: 100%; height: 228px; background: var(--paper); }
  .back__band {
    position: absolute; left: 136px; top: 332px; width: 245px; height: 55px;
    background: var(--gold); border-radius: 28px 0 0 28px;
  }
  .back__emblem {
    position: absolute; left: 160px; top: 134px; width: 60px; height: 60px;
    border-radius: 50%; background: var(--gold);
  }
  .back__small-name {
    position: absolute; left: 0; width: 100%; top: 213px; text-align: center;
    color: var(--paper); font-weight: 500; font-size: 12px; letter-spacing: 4px;
  }
  .back__name {
    position: absolute; left: 0; width: 100%; top: 456px; text-align: center;
    color: var(--gold); font-weight: 900; font-size: 28px; letter-spacing: 11px; padding-left: 11px;
  }
  .back__tagline {
    position: absolute; left: 0; width: 100%; top: 494px; text-align: center;
    color: var(--gold); font-weight: 500; font-size: 8px; letter-spacing: 2px;
  }
</style>
</head>
<body>
  <section class="card card--front">
    <div class="front__paper"></div>
    <div class="vertical front__name"><span class="front__dot"></span>lumo4kart</div>
    <div class="vertical front__tagline">EFTPOS | ONLINE | MOBILE</div>
    <div class="front__tab"><span class="front__tab-name">lumo4kart</span></div>
    <ul class="contact">
      <li class="contact__item">lumo4kart.com.au</li>
      <li class="contact__item">contact@lumo4kart.com.au</li>
      <li class="contact__item">0432 587 904</li>
      <li class="contact__item">02 6815 3927</li>
    </ul>
  </section>

  <section class="card card--back">
    <div class="back__emblem"></div>
    <div class="back__small-name">lumo4kart</div>
    <div class="back__paper"></div>
    <div class="back__band"></div>
    <div class="back__name">lumo4kart</div>
    <div class="back__tagline">EFTPOS | ONLINE | MOBILE</div>
  </section>
</body>
</html>
```